New Business Card for Auto Repair and Performance Shop!

Need a redesign on a card that we have used for a while now. Something more update and modern, Serious but not too serious. Something confident, that shows the client that we are bespoke. Adding value.

Target Market(s)

Foreign Auto Repair and Performance

Industry/Entity Type

Automotive

Contact Information for Business Card

Utilize Logo, would like to change car silhouette to something Veltra,

Font styles to use
Sans Serif

Requirements
Must have
• business name, address, website, phone number.
MotoSerenix
4918 W. Birchwell Rd
Killeen, T.X. 76542
1-254-487-3106
www.moto-serenix-example.com

Specializing in Asian, European, and Domestic Auto Repair, Performance and Fabrication.

Clear space on back to for space to write appointment time and which client advisor helped the client.
Nice to have
• Up to the designers,

```html
<!DOCTYPE html>
<html lang="en">
<head>
<meta charset="UTF-8">
<title>MotoSerenix – Business Card</title>
<link href="https://fonts.googleapis.com/css2?family=Lato:wght@400;700&display=swap" rel="stylesheet">
<style>
  :root {
    --bg: #e6e4e1;
    --card-dark: #222223;
    --card-light: #ffffff;
    --accent-red: #b3151b;
    --text-light: #f2f2f2;
    --text-muted: #a8a8a8;
    --text-dark: #333333;
    --logo-ink: #1c1c1c;
  }
  * { box-sizing: border-box; margin: 0; padding: 0; }
  html, body {
    width: 1200px; height: 900px; overflow: hidden;
    background: var(--bg);
    font-family: "Lato", sans-serif;
  }
  .canvas { position: relative; width: 1200px; height: 900px; }
  .card {
    position: absolute; left: 280px;
    width: 640px; height: 366px;
    border-radius: 34px;
    overflow: hidden;
    box-shadow: 0 6px 18px rgba(0,0,0,0.18);
  }
  /* Contact side */
  .card--contact { top: 58px; background: var(--card-dark); color: var(--text-light); }
  .accent-bar {
    position: absolute; width: 12px; height: 120px;
    background: var(--accent-red);
  }
  .accent-bar--left { left: 0; top: 40px; }
  .accent-bar--right { right: 0; bottom: 40px; }
  .holder {
    position: absolute; left: 40px; top: 112px; width: 160px;
    text-align: right; white-space: nowrap;
  }
  .holder__name { font-size: 26px; font-weight: 700; letter-spacing: -0.4px; }
  .holder__name span { font-weight: 400; }
  .holder__role { font-size: 15px; color: var(--text-muted); margin-top: 2px; }
  .contact-list {
    position: absolute; left: 224px; top: 115px;
    list-style: none;
  }
  .contact-list li {
    display: flex; align-items: center; height: 34px;
    font-size: 17px; letter-spacing: 0.1px; white-space: nowrap;
  }
  .contact-list svg {
    width: 18px; height: 18px; margin-right: 20px; flex: none;
    fill: var(--text-light); stroke: var(--text-light);
  }
  /* Appointment side */
  .card--appointment { top: 476px; background: var(--card-light); color: var(--text-dark); }
  .brand {
    position: absolute; right: 70px; top: 58px;
    display: flex; align-items: center; gap: 14px;
  }
  .brand__mark { width: 22px; height: 22px; border-radius: 50%; background: var(--logo-ink); }
  .brand__name { font-size: 44px; font-weight: 700; color: var(--logo-ink); letter-spacing: 0.5px; }
  .tagline {
    position: absolute; right: 56px; top: 140px; width: 470px;
    text-align: right; color: var(--accent-red);
    font-size: 18px; font-weight: 400; text-transform: uppercase;
    line-height: 1.35; letter-spacing: 0.2px;
  }
  .appointment {
    position: absolute; left: 56px; top: 232px;
    font-size: 19px; color: var(--text-dark);
  }
  .appointment__row { display: flex; align-items: flex-end; height: 40px; }
  .appointment__label { width: 180px; }
  .appointment__line {
    width: 300px; border-bottom: 1px solid #c9c9c9; margin-left: 10px; height: 22px;
  }
</style>
</head>
<body>
<main class="canvas">

  <section class="card card--contact" aria-label="Contact side">
    <div class="accent-bar accent-bar--left"></div>
    <div class="accent-bar accent-bar--right"></div>

    <div class="holder">
      <p class="holder__name">Lorem <span>ipsum</span></p>
      <p class="holder__role">founder</p>
    </div>

    <ul class="contact-list">
      <li>
        <svg viewBox="0 0 24 24" stroke-width="0"><path d="M6.6 10.8a15.1 15.1 0 0 0 6.6 6.6l2.2-2.2a1 1 0 0 1 1-.25 11.4 11.4 0 0 0 3.6.57 1 1 0 0 1 1 1V20a1 1 0 0 1-1 1A17 17 0 0 1 3 4a1 1 0 0 1 1-1h3.5a1 1 0 0 1 1 1c0 1.25.2 2.45.57 3.57a1 1 0 0 1-.25 1z"/></svg>
        1-254-487-3106
      </li>
      <li>
        <svg viewBox="0 0 24 24" stroke-width="0"><path d="M2 21l21-9L2 3v7l15 2-15 2z"/></svg>
        info@moto-serenix-example.com
      </li>
      <li>
        <svg viewBox="0 0 24 24" fill="none" stroke-width="1.6"><circle cx="12" cy="12" r="9.5" fill="none"/><ellipse cx="12" cy="12" rx="4" ry="9.5" fill="none"/><path d="M2.5 12h19M4 7h16M4 17h16" fill="none"/></svg>
        www.moto-serenix-example.com
      </li>
      <li>
        <svg viewBox="0 0 24 24" stroke-width="0"><path d="M12 3l10 9h-3v9h-5v-6h-4v6H5v-9H2z"/></svg>
        4918 W. Birchwell Rd Killeen, T.X. 76542
      </li>
    </ul>
  </section>

  <section class="card card--appointment" aria-label="Appointment side">
    <div class="brand">
      <span class="brand__mark"></span>
      <span class="brand__name">MotoSerenix</span>
    </div>

    <p class="tagline">Specializing in Asian, European, and Domestic Auto Repair, Performance and Fabrication.</p>

    <div class="appointment">
      <div class="appointment__row">
        <span class="appointment__label">Appointment time</span>:
        <span class="appointment__line"></span>
      </div>
      <div class="appointment__row">
        <span class="appointment__label">Client-advisor</span>:
        <span class="appointment__line"></span>
      </div>
    </div>
  </section>

</main>
</body>
</html>
```